Valbrook Data Works

Our company is about IT hardwares and IT solutions. IT hardware such as PC, RAMS, storage and servers. IT solutions such as project management, BA. We are also selling new technology too.

Target Market(s)

Consumer, Small to Medium Business, Corporate

Requirements
Must have
• The business card must have the following:
• Name:
• Title:
• Contact Number:
• Email address:
• Website:
• Color: Must match the logo color upgrade

```html
<!DOCTYPE html>
<html lang="en">
<head>
<meta charset="utf-8">
<title>Valbrook Data Works – Business Card</title>
<link rel="stylesheet" href="https://fonts.googleapis.com/css2?family=Saira:wght@700&family=Roboto:wght@400;700&display=swap">
<style>
  :root {
    --stage: #3b3430;
    --card: #151515;
    --card-edge: #1f1f1f;
    --ink: #f4f4f4;
    --accent: #e08a1e;
  }
  html, body {
    margin: 0;
    width: 1200px;
    height: 780px;
    overflow: hidden;
    background: var(--stage);
  }
  .stage {
    position: relative;
    width: 1200px;
    height: 780px;
  }
  .card {
    position: absolute;
    width: 540px;
    height: 309px;
    background: radial-gradient(circle at 40% 35%, #222 0%, var(--card) 70%);
    border: 1px solid var(--card-edge);
    box-shadow: 0 12px 30px rgba(0,0,0,.45);
    box-sizing: border-box;
    font-family: "Roboto", Arial, sans-serif;
    color: var(--ink);
    overflow: hidden;
  }
  .card--front { left: 50px; top: 110px; }
  .card--back { left: 610px; top: 360px; }

  .brand {
    display: flex;
    align-items: center;
    gap: 10px;
  }
  .brand__mark {
    width: 14px;
    height: 14px;
    background: var(--accent);
    flex: none;
  }
  .brand__name {
    font-family: "Saira", Arial, sans-serif;
    font-weight: 700;
    color: var(--ink);
    text-transform: uppercase;
    letter-spacing: .5px;
    line-height: 1;
    white-space: nowrap;
  }
  .card--front .brand {
    position: absolute;
    left: 0; right: 0; top: 130px;
    justify-content: center;
  }
  .card--front .brand__name { font-size: 34px; }

  .card--back .brand {
    position: absolute;
    right: 32px; top: 48px;
  }
  .card--back .brand__mark { width: 12px; height: 12px; }
  .card--back .brand__name { font-size: 24px; }

  .person {
    position: absolute;
    left: 34px; top: 104px;
  }
  .person__name {
    margin: 0;
    font-weight: 700;
    font-size: 15px;
    letter-spacing: .5px;
    text-transform: uppercase;
  }
  .person__title {
    margin: 2px 0 0;
    font-size: 13px;
    color: var(--accent);
  }
  .person__rule {
    width: 58px;
    height: 1px;
    background: var(--accent);
    margin: 6px 0 10px;
  }
  .contact {
    list-style: none;
    margin: 0; padding: 0;
    font-size: 13px;
  }
  .contact li {
    display: flex;
    align-items: center;
    gap: 8px;
    margin-bottom: 4px;
    white-space: nowrap;
  }
  .contact svg { width: 11px; height: 11px; fill: var(--accent); flex: none; }

  .divider {
    position: absolute;
    left: 34px; right: 60px; top: 228px;
    height: 1px;
    background: var(--accent);
  }
  .address {
    position: absolute;
    right: 32px; bottom: 22px;
    margin: 0;
    font-size: 14px;
    font-style: normal;
    line-height: 1.35;
  }
</style>
</head>
<body>
<main class="stage">
  <section class="card card--front" aria-label="Card front">
    <div class="brand">
      <span class="brand__mark"></span>
      <span class="brand__name">Valbrook Data Works</span>
    </div>
  </section>

  <section class="card card--back" aria-label="Card back">
    <div class="brand">
      <span class="brand__mark"></span>
      <span class="brand__name">Valbrook Data Works</span>
    </div>

    <div class="person">
      <h1 class="person__name">Mara Ellison</h1>
      <p class="person__title">Manager</p>
      <div class="person__rule"></div>
      <ul class="contact">
        <li>
          <svg viewBox="0 0 12 12" aria-hidden="true"><path d="M2.5 0.5l2 2.5-1.2 1.3c.7 1.6 2 2.9 3.6 3.6L8.2 6.7l2.5 2-1 2.3C4.8 11 1 7.2 0.5 2.3z"/></svg>
          555-214-0893
        </li>
        <li>
          <svg viewBox="0 0 12 12" aria-hidden="true"><path d="M0 2h12v8H0z M0.8 2.6L6 6.6l5.2-4H0.8z" fill-rule="evenodd"/></svg>
          hello@valbrookdata.com
        </li>
        <li>
          <svg viewBox="0 0 12 12" aria-hidden="true"><circle cx="6" cy="6" r="5.5"/></svg>
          www.valbrookdata.com
        </li>
      </ul>
    </div>

    <div class="divider"></div>

    <address class="address">PO BOX 418 Harlow Lane<br>7th street Ashford</address>
  </section>
</main>
</body>
</html>
```